Commercial Swimming Pool - Design-Build Contractor Website Design

I need a new website that will feature our newly developed logo and trade name as well as provide a fully updated site experience. We are not a residential builder - we strictly design and install high-end commercial pools. I need the website to highlight our portfolio and communicate the various types of projects in which we specialize. I want the effect of the site to reflect the high-end nature of our services - projects like the 57th floor spa at the Delmar Brightwater, the aquatic therapy portion of the Delmar Falcons training facility, a 5om indoor competition pool for the prestigious Thornwick Academy, the indoor water park at The Calloway Lodge or the recent country club renovation projects we've completed in our region (to name a few examples).

```html
<!DOCTYPE html>
<html lang="en">
<head>
<meta charset="utf-8">
<title>Corwen Aquatics – Commercial Pool Design &amp; Construction</title>
<link href="https://fonts.googleapis.com/css2?family=Josefin+Sans:wght@300;400;600;700&display=swap" rel="stylesheet">
<style>
  :root{
    --navy:#1f3a5c;
    --navy-dark:#13294a;
    --sky:#29a8e0;
    --projects-bg:#2d5175;
    --ink:#1a1a1a;
    --muted:#8a8a8a;
    --ghost:#ececec;
    --paper:#ffffff;
    --mist:#f2f2f2;
  }
  *{box-sizing:border-box;margin:0;padding:0}
  html,body{width:1200px;height:3589px;overflow:hidden}
  body{font-family:"Josefin Sans",Arial,sans-serif;color:var(--ink);background:var(--paper);position:relative}
  .abs{position:absolute}

  /* header */
  .site-header{position:absolute;left:0;top:0;width:1200px;height:94px;background:var(--paper)}
  .brand{position:absolute;display:flex;align-items:center;gap:10px;color:var(--navy);font-weight:600;letter-spacing:1px;line-height:1}
  .brand-dot{background:var(--sky);border-radius:50%;flex:none}
  .site-header .brand{left:112px;top:26px;font-size:28px}
  .site-header .brand-dot{width:30px;height:30px}
  .nav{position:absolute;list-style:none;font-size:18px;color:var(--ink)}
  .nav li{position:absolute;white-space:nowrap}

  /* hero */
  .hero{position:absolute;left:0;top:94px;width:1200px;height:606px;
    background:linear-gradient(90deg,#5d8fc4 0%,#9cc4e6 30%,#cfe3f2 55%,#e9f1f7 80%,#f4f6f8 100%)}
  .hero-pool{position:absolute;left:0;top:260px;width:1200px;height:346px;
    background:linear-gradient(180deg,#2f7fb9 0%,#4fb9de 40%,#d9e6ee 75%,#eef1f4 100%);opacity:.75}
  .hero-rule{position:absolute;left:0;top:700px;width:1200px;height:6px;background:var(--navy-dark)}
  .hero-kicker{left:571px;top:232px;font-size:44px;font-weight:400;color:#111;letter-spacing:1px}
  .hero-title{left:571px;top:284px;font-size:56px;font-weight:700;color:#111;letter-spacing:1px;white-space:nowrap}
  .hero-copy{left:571px;top:364px;width:380px;font-size:14.5px;font-weight:600;line-height:21px;color:#111}

  .btn{position:absolute;display:flex;align-items:center;justify-content:center;background:var(--navy);color:#fff;font-weight:600;font-size:17px}
  .btn::after{content:"";position:absolute;left:7px;top:7px;right:-7px;bottom:-7px;border:2px solid var(--sky);z-index:-1}
  .btn-wrap{position:absolute;z-index:1}

  /* about */
  .ghost{position:absolute;font-weight:700;color:var(--ghost);letter-spacing:4px;line-height:1}
  .section-title{position:absolute;font-weight:700;font-size:34px;letter-spacing:1px;white-space:nowrap}
  .about-lead{left:268px;top:944px;width:680px;font-size:18.5px;line-height:28.5px;color:#222}
  .about-col{top:1048px;width:310px;font-size:13.5px;font-weight:300;line-height:23.5px;color:var(--muted)}

  /* projects */
  .projects{position:absolute;left:0;top:1347px;width:1200px;height:807px;
    background:radial-gradient(ellipse at 30% 40%,#36608a 0%,#2d5175 55%,#284a6c 100%)}
  .projects .ghost{color:rgba(20,40,65,.35)}
  .projects-ring{position:absolute;left:750px;top:1580px;width:340px;height:340px;border-radius:50%;border:44px solid rgba(30,60,95,.35)}
  .projects-lead{left:374px;top:1552px;width:720px;font-size:17px;line-height:28.5px;color:#fff}
  .project{position:absolute;top:1676px;width:315px}
  .project-photo{width:315px;height:262px}
  .project-caption{margin-top:22px;font-size:16px;font-weight:400;line-height:28px;color:#fff;letter-spacing:.3px;text-transform:uppercase}

  /* services */
  .services-photo{position:absolute;left:0;top:2154px;width:598px;height:571px;
    background:linear-gradient(180deg,#3d6fa0 0%,#6fb4d8 25%,#4fb3dc 55%,#2e93c6 100%)}
  .services-lead{left:657px;top:2268px;width:430px;font-size:20px;font-weight:600;line-height:32.5px;color:#555}
  .service{position:absolute;left:673px;width:413px;height:82px}
  .service-box{position:absolute;left:35px;top:0;width:378px;height:82px;border:2.5px solid var(--sky);background:#fff}
  .service-icon{position:absolute;left:0;top:7px;width:68px;height:68px}
  .service-label{position:absolute;left:87px;top:26px;font-size:27px;font-weight:300;color:#333}

  /* gallery */
  .gallery{position:absolute;left:0;top:2725px;width:1200px;height:649px;background:var(--mist)}
  .gallery-water{position:absolute;left:0;top:2899px;width:1200px;height:475px;
    background:linear-gradient(180deg,#eaf6fb 0%,#7fd0ec 35%,#3bb4e0 70%,#5cc3e6 100%)}
  .gallery-panels{position:absolute;left:0;top:2899px}
  .pager{position:absolute;top:3265px;width:48px;height:36px;border:1.5px solid #c9b88a;display:flex;align-items:center;justify-content:center}

  /* footer */
  .site-footer{position:absolute;left:0;top:3374px;width:1200px;height:215px;background:var(--paper)}
  .footer-brand{position:absolute;left:118px;top:3448px;display:flex;align-items:center;gap:16px;color:var(--navy);font-weight:600;font-size:44px;letter-spacing:2px;line-height:46px}
  .footer-brand .brand-dot{width:48px;height:48px}
  .copyright{position:absolute;right:113px;top:3518px;font-size:14px;font-weight:400;color:#111;white-space:nowrap}
</style>
</head>
<body>

<header class="site-header">
  <div class="brand"><span class="brand-dot"></span>CORWEN AQUATICS</div>
  <ul class="nav" style="top:38px">
    <li style="left:631px">Home</li>
    <li style="left:727px">About Us</li>
    <li style="left:850px">Our Services</li>
    <li style="left:999px">Contact Us</li>
  </ul>
</header>

<section class="hero" role="img" aria-label="Cabana with white curtains on a terrace beside an infinity pool overlooking the sea">
  <div class="hero-pool"></div>
</section>
<div class="hero-rule"></div>
<div class="abs hero-kicker">WELCOME TO</div>
<h1 class="abs hero-title">CORWEN AQUATICS</h1>
<p class="abs hero-copy">Lorem ipsum dolor sit amet, consectetur adipiscing elit, sed do eiusmod tempor incididunt ut labore et dolore magna aliqua.</p>
<div class="btn-wrap" style="left:571px;top:443px;width:169px;height:48px">
  <a class="btn" style="left:0;top:0;width:169px;height:48px">Get Started</a>
</div>

<!-- about -->
<div class="ghost" style="left:70px;top:800px;font-size:128px">ABOUT</div>
<h2 class="section-title" style="left:265px;top:888px">INSTALL HIGH-END COMMERCIAL POOLS</h2>
<p class="abs about-lead">Lorem ipsum dolor sit amet, consectetur adipiscing elit, sed do eiusmod tempor incididunt ut labore et dolore magna aliqua. Ut enim ad minim veniam, quis nostrud exercitation ullamco laboris nisi ut aliquip ex ea commodo consequat</p>
<p class="abs about-col" style="left:268px">Lorem ipsum dolor sit amet, consectetur adipiscing elit, sed do eiusmod tempor incididunt ut labore et dolore magna aliqua. Ut enim ad minim veniam, quis nostrud exercitation ullamco laboris nisi ut aliquip ex ea commodo consequat</p>
<p class="abs about-col" style="left:631px">Lorem ipsum dolor sit amet, consectetur adipiscing elit, sed do eiusmod tempor incididunt ut labore et dolore magna aliqua. Ut enim ad minim veniam, quis nostrud exercitation ullamco laboris nisi ut aliquip ex ea commodo consequat</p>
<div class="btn-wrap" style="left:275px;top:1196px;width:168px;height:47px">
  <a class="btn" style="left:0;top:0;width:168px;height:47px">Read More</a>
</div>

<!-- projects -->
<section class="projects">
  <div class="ghost" style="left:75px;top:54px;font-size:128px">WORK</div>
</section>
<div class="projects-ring"></div>
<h2 class="section-title" style="left:370px;top:1486px;color:#fff">OUR&nbsp; PROJECTS</h2>
<p class="abs projects-lead">Lorem ipsum dolor sit amet, consectetur adipiscing elit, sed do eiusmod tempor incididunt ut labore et dolore magna aliqua. Ut enim ad minim veniam, quis nostrud exercitation</p>

<article class="project" style="left:112px">
  <div class="project-photo" role="img" aria-label="Rooftop spa pool with fountain among palm trees" style="background:linear-gradient(180deg,#d9ecf6 0%,#7fa86a 40%,#2a7fd0 70%,#1656b0 100%)"></div>
  <p class="project-caption">57th floor spa at the Delmar<br>Brightwater</p>
</article>
<article class="project" style="left:442px">
  <div class="project-photo" role="img" aria-label="Resort garden with palm trees leading to a therapy pool deck" style="background:linear-gradient(180deg,#b9d3e8 0%,#5e8a4a 45%,#8a9a70 75%,#d8d2c0 100%)"></div>
  <p class="project-caption">The aquatic therapy portion<br>of the Delmar Falcons training</p>
</article>
<article class="project" style="left:772px">
  <div class="project-photo" role="img" aria-label="Indoor competition pool under a glass roof" style="background:linear-gradient(180deg,#d4dde4 0%,#9aa9b4 35%,#2e9fd6 70%,#1f6ea8 100%)"></div>
  <p class="project-caption">A 50m indoor competition<br>pool for the prestigious<br>Thornwick Academy</p>
</article>

<!-- services -->
<div class="services-photo" role="img" aria-label="Swimmer doing butterfly stroke in a competition pool lane"></div>
<h2 class="section-title" style="left:655px;top:2210px;font-size:36px">OUR SERVICES</h2>
<p class="abs services-lead">Lorem ipsum dolor sit amet, consectetur adipiscing elit, sed do eiusmod tempor incididunt ut labore et dolore magna aliqua.</p>

<div class="service" style="top:2385px">
  <div class="service-box"></div>
  <svg class="service-icon" viewBox="0 0 68 68" aria-hidden="true"><circle cx="34" cy="34" r="33" fill="var(--navy)"/><circle cx="34" cy="34" r="27" fill="none" stroke="#fff" stroke-width="1.2"/><rect x="22" y="22" width="22" height="22" fill="none" stroke="#fff" stroke-width="2"/><path d="M25 41 L43 23" stroke="#fff" stroke-width="2"/></svg>
  <span class="service-label">Design</span>
</div>
<div class="service" style="top:2497px">
  <div class="service-box"></div>
  <svg class="service-icon" viewBox="0 0 68 68" aria-hidden="true"><circle cx="34" cy="34" r="33" fill="var(--navy)"/><circle cx="34" cy="34" r="27" fill="none" stroke="#fff" stroke-width="1.2"/><path d="M20 38h28v10H20zM20 43h28M27 38v5M34 43v5M41 38v5" fill="none" stroke="#fff" stroke-width="2"/></svg>
  <span class="service-label">Construction</span>
</div>
<div class="service" style="top:2607px">
  <div class="service-box"></div>
  <svg class="service-icon" viewBox="0 0 68 68" aria-hidden="true"><circle cx="34" cy="34" r="33" fill="var(--navy)"/><circle cx="34" cy="34" r="27" fill="none" stroke="#fff" stroke-width="1.2"/><circle cx="34" cy="34" r="15" fill="none" stroke="#fff" stroke-width="2"/><circle cx="34" cy="34" r="8" fill="none" stroke="#fff" stroke-width="2"/><circle cx="34" cy="34" r="2.5" fill="#fff"/></svg>
  <span class="service-label">Excellence</span>
</div>

<!-- gallery -->
<section class="gallery">
  <div class="ghost" style="left:66px;top:44px;font-size:128px">GALLERY</div>
</section>
<div class="gallery-water" role="img" aria-label="Person in a sun hat resting at the edge of a bright blue pool"></div>
<h2 class="section-title" style="left:467px;top:2858px">OUR PORTFOLIO</h2>
<svg class="gallery-panels" width="1200" height="475" viewBox="0 0 1200 475">
  <defs>
    <linearGradient id="lanes" x1="0" y1="0" x2="1" y2="1"><stop offset="0" stop-color="#6fd0f0"/><stop offset="1" stop-color="#1e9fd8"/></linearGradient>
    <linearGradient id="resort" x1="0" y1="0" x2="0" y2="1"><stop offset="0" stop-color="#8ccbe8"/><stop offset=".45" stop-color="#4f7d3a"/><stop offset=".7" stop-color="#1d9fd0"/><stop offset="1" stop-color="#0e6fa8"/></linearGradient>
    <linearGradient id="palms" x1="0" y1="0" x2="0" y2="1"><stop offset="0" stop-color="#f3e4c2"/><stop offset=".45" stop-color="#b89a6a"/><stop offset=".75" stop-color="#5fb8c8"/><stop offset="1" stop-color="#8a7a60"/></linearGradient>
  </defs>
  <polygon points="100,4 416,16 416,316 100,326" fill="url(#lanes)" role="img" aria-label="Lane rope across a competition pool"/>
  <rect x="436" y="36" width="329" height="286" fill="url(#resort)" role="img" aria-label="Resort pool with umbrellas and palm trees"/>
  <polygon points="782,20 1098,3 1098,363 782,328" fill="url(#palms)" role="img" aria-label="Palm-lined resort pool at sunset"/>
</svg>
<div class="pager" style="left:548px"><svg width="30" height="12" viewBox="0 0 30 12"><path d="M29 6H3M8 1L2 6l6 5" fill="none" stroke="#111" stroke-width="2.5"/></svg></div>
<div class="pager" style="left:602px"><svg width="30" height="12" viewBox="0 0 30 12"><path d="M1 6h26M22 1l6 5-6 5" fill="none" stroke="#111" stroke-width="2.5"/></svg></div>

<!-- footer -->
<footer class="site-footer"></footer>
<div class="footer-brand"><span class="brand-dot"></span><span>CORWEN<br>AQUATICS</span></div>
<ul class="nav" style="top:3457px">
  <li style="left:630px">Home</li>
  <li style="left:726px">About Us</li>
  <li style="left:849px">Our Services</li>
  <li style="left:998px">Contact Us</li>
</ul>
<p class="copyright">Copyright © 2023 Corwen Aquatics, Inc All Rights Reserved</p>

</body>
</html>
```